Divorce Lawyer Creative Business Card Design Project

Need a fresh look for our business cards that incorporates our current logo. We have three attorneys and six staff. Some will also use a Q/R Code (which is personal to the staff member) and that should be incorporated into the design so that we have a "with Q/R Code option" and a "without Q/R Code option"
While our business is serious and we want to be professional, we also welcome a bit of creativity and "fun." See http://quillmarten.example/creative-business-card-for-a-divorce-lawyer/ for a unique divorce lawyer business card. It is cool but the card itself is boring...
We add new people, change titles, some of our staff get married (and divorced) and have name changes and we need the ability to use a design template that you provide to make these changes ourselves. We usually print our cards at Orno Press.
I have uploaded a file that contains a sample of our current front and back of the business card as well as a sample Q/R Contact code to be included on a card. Obviously, we like the design that we have which should give you a feel for us but we are ready for a fresh look.
If you can't provide a design that we can manipulate, we will need .eps, .pdf, and .jpg files for three attorneys and six staff.
Updates
- Layout for this card is really nice: http://blog.inkholt.example/wp-content/uploads/2013/03/tovra-business-card.jpg
- This is creative: http://pinboardly.example/pin/502817364920175438/ but I don't really like it.
- Plastic is kind of cool: http://pinboardly.example/pin/502817364920331642/
- DISLIKE: http://brandvaultly.example/sites/default/files/styles/media/public/images/Lawyerbusinesscard.jpg?itok=ZmRtWx-k
- This is really cool but I fear the printing costs would be too high: http://pinboardly.example/pin/61520487390254718/
- I am not opposed to different but similar designs: See http://www.folionest.example/gallery/ZEP-Business-Cards/8260534
Industry/Entity Type
Lawyer
Requirements
Must have
- Our Logo
Person's Full Name
Title
Phone #
Fax #
Email
Web Address

```html
<!DOCTYPE html>
<html lang="en">
<head>
<meta charset="utf-8">
<title>Harrow Family Law – Business Cards</title>
<link rel="stylesheet" href="https://fonts.googleapis.com/css2?family=Open+Sans:wght@300;400&display=swap">
<style>
  :root {
    --backdrop: #3a3a3c;
    --ink: #1e1e1e;
    --paper: #ffffff;
    --accent: #b5d334;
    --muted: #d8d8d8;
  }
  html, body {
    margin: 0;
    width: 1200px;
    height: 900px;
    overflow: hidden;
    background: var(--backdrop);
    font-family: "Open Sans", sans-serif;
  }
  .card-row {
    position: absolute;
    left: 80px;
    top: 270px;
    display: flex;
    gap: 40px;
  }
  .card {
    width: 230px;
    height: 360px;
    display: block;
    overflow: visible;
  }
  .card text { font-family: "Open Sans", sans-serif; }
  .fill-ink { fill: var(--ink); }
  .fill-paper { fill: var(--paper); }
  .fill-accent { fill: var(--accent); }
  .word-large { font-size: 17px; font-weight: 400; }
  .person-name { font-size: 12.5px; font-weight: 400; }
  .person-title { font-size: 9.5px; font-weight: 300; }
  .contact-line { font-size: 8.6px; font-weight: 300; }
  .band-title { font-size: 14px; font-weight: 300; }
</style>
</head>
<body>
<main class="card-row">

  <!-- Front, dark -->
  <svg class="card card-front-dark" viewBox="0 0 230 360" aria-label="Business card front, dark">
    <path class="fill-ink" d="M28 0 H230 V200 L0 232 V28 Q0 0 28 0 Z"/>
    <path class="fill-ink" d="M0 240 L230 206 V332 Q230 360 202 360 H0 Z"/>
    <rect class="fill-paper" x="20" y="0" width="190" height="11"/>
    <text class="fill-paper word-large" x="14" y="226" transform="rotate(-8 14 226)">Divorce</text>
    <text class="fill-paper word-large" x="18" y="268" transform="rotate(-8 18 268)">Lawyer</text>
    <text class="fill-paper person-name" x="98" y="198" transform="rotate(-8 98 198)">Daniel Hartley Moore</text>
    <text class="fill-paper person-title" x="104" y="212" transform="rotate(-8 104 212)">Managing Attorney</text>
  </svg>

  <!-- Front, light -->
  <svg class="card card-front-light" viewBox="0 0 230 360" aria-label="Business card front, light">
    <path class="fill-paper" d="M28 0 H230 V200 L0 232 V28 Q0 0 28 0 Z"/>
    <path class="fill-paper" d="M0 240 L230 206 V332 Q230 360 202 360 H0 Z"/>
    <rect class="fill-ink" x="20" y="0" width="190" height="11"/>
    <text class="fill-ink word-large" x="14" y="226" transform="rotate(-8 14 226)">Divorce</text>
    <text class="fill-ink word-large" x="18" y="268" transform="rotate(-8 18 268)">Lawyer</text>
    <text class="fill-ink person-name" x="98" y="198" transform="rotate(-8 98 198)">Daniel Hartley Moore</text>
    <text class="fill-ink person-title" x="104" y="212" transform="rotate(-8 104 212)">Managing Attorney</text>
  </svg>

  <!-- Back, contact details -->
  <svg class="card card-back-contact" viewBox="0 0 230 360" aria-label="Business card back with contact details">
    <path class="fill-ink" d="M0 0 H230 V360 H28 Q0 360 0 332 Z"/>
    <rect class="fill-paper" x="20" y="0" width="110" height="11"/>
    <g class="contact-list">
      <circle class="fill-paper" cx="22" cy="176" r="2.2"/>
      <text class="fill-paper contact-line" x="32" y="179">Lantern Court-Suite B 218 Alder street</text>
      <text class="fill-paper contact-line" x="32" y="195">Marlow Bay, NC 28999</text>
      <circle class="fill-paper" cx="22" cy="208" r="2.2"/>
      <text class="fill-paper contact-line" x="32" y="211">Phone - 910 555 0142</text>
      <circle class="fill-paper" cx="22" cy="224" r="2.2"/>
      <text class="fill-paper contact-line" x="32" y="227">Email - dmoore@harrowfamilylaw.example</text>
      <circle class="fill-paper" cx="22" cy="240" r="2.2"/>
      <text class="fill-paper contact-line" x="32" y="243">Web - www.harrowfamilylaw.example</text>
    </g>
  </svg>

  <!-- Back, title band -->
  <svg class="card card-back-title" viewBox="0 0 230 360" aria-label="Business card back with title band">
    <path class="fill-paper" d="M0 0 H202 Q230 0 230 28 V360 H0 Z"/>
    <rect class="fill-accent" x="0" y="150" width="230" height="56"/>
    <text class="fill-paper band-title" x="115" y="183" text-anchor="middle">Managing Attorney</text>
    <rect class="fill-ink" x="0" y="330" width="150" height="11"/>
  </svg>

</main>
</body>
</html>
```